Wenna's Atelier, Beauty & Therapy. New business in Verbier, Switzerland

Simple Flyer to put in evidence a particular service that the studio offers that is
EMS ( ELECTRIC MUSCLE STIMULATION)
There is a bike festival in Verbier ion the 12th of August and i would like to take an opportunity of this slot to advertise our new suit of EMS that can be very helpful for bike riders. The product is a suit with muscle electrostimulation, And there are many advantages and functionnality. For sportsmen and women, it can
I don't have any particular picture be cause the product is very new.
But i can send you some images for you to understand what it is, but if you find some images on the web it is better :)
I upload different versions of Logo, PLEASE FEEL FREE TO CHOOSE WHAT IS BEST :)
please check this link for more information about the product applied for bikers
https://www.pulvaro-suits.example/en/cycling-training-with-muscle-electrostimulation/
Updates
Hello Designers,
Here are a few details concerning the project;
- Wenna's Atelier is not a reseller of the EMS suits, but we provide it as a service inside our studio.
- We wish to communicate on this new technology in order to bring a maximum of attention, not only for the suit, but also for the brand it self, since it is new in Verbier.
- for the flyer, i would like it to be simple, appealing, and without too much text.
- a french version of the same flyer is appreciated, without extra cost ;)
Thanks
Hello all designers,
thank you for all the good work.
For you who mentioned a date for the festival, i suggest please to take it off, and keep only " Alpen Pedal Gathering" if you want.
Thank you

```html
<!DOCTYPE html>
<html lang="en">
<head>
<meta charset="UTF-8">
<title>Wenna's Atelier – EMS Flyers</title>
<link href="https://fonts.googleapis.com/css2?family=Lexend:wght@200;300;400;500;600&display=swap" rel="stylesheet">
<style>
  :root{
    --stage:#200a1e;
    --plum:#6b1c5a;
    --paper-top:#f8ebe6;
    --paper-bottom:#fdf7f4;
    --white:#ffffff;
    --photo-a:#e9dfdc;
    --photo-b:#4a4650;
  }
  *{margin:0;padding:0;box-sizing:border-box}
  html,body{width:1200px;height:1200px;overflow:hidden;background:var(--stage)}
  body{position:relative;font-family:"Lexend",sans-serif;color:var(--plum)}

  .flyer{position:absolute;top:220px;width:542px;height:759px;overflow:hidden;
    background:radial-gradient(ellipse at 50% 30%,var(--paper-top),var(--paper-bottom) 70%)}
  .flyer--en{left:41px}
  .flyer--fr{left:617px}

  .flyer__shapes{position:absolute;inset:0}

  .brand{position:absolute;left:0;right:0;top:17px;text-align:center}
  .brand__ring{width:90px;height:90px;margin:0 auto;border:5px solid var(--plum);border-radius:50%}
  .brand__name{margin-top:18px;font-size:21px;font-weight:500;letter-spacing:5px;text-transform:uppercase;color:var(--plum)}

  .kicker{position:absolute;left:0;right:0;top:158px;text-align:center;font-size:15px;font-weight:200;color:var(--plum)}
  .headline{position:absolute;left:0;right:0;top:184px;text-align:center;font-size:30px;font-weight:600;letter-spacing:-0.6px;color:var(--plum);white-space:nowrap}
  .tagline{position:absolute;left:48px;width:445px;top:230px;border:1.5px solid var(--plum);border-radius:6px;
    font-size:11.4px;font-weight:500;text-align:center;line-height:15px;padding:3px 6px;color:var(--plum)}
  .flyer--fr .tagline{left:29px;width:482px;top:227px;padding:2px 6px}

  .event{position:absolute;left:153px;width:232px;top:263px;height:22px;background:var(--plum);color:var(--white);
    font-size:14px;font-weight:400;text-align:center;line-height:22px;
    clip-path:polygon(0 0,100% 0,94% 50%,100% 100%,0 100%,6% 50%)}
  .flyer--fr .event{top:269px}

  .photo{position:absolute;left:230px;top:301px;width:290px;height:428px;border-radius:40% 40% 6px 6px;
    background:linear-gradient(160deg,var(--photo-a) 0%,var(--photo-b) 55%,#2a2730 100%);opacity:.85}

  .benefits__tag{position:absolute;left:0;top:455px;width:135px;height:21px;background:var(--plum);color:var(--white);
    font-size:16px;font-weight:400;line-height:21px;padding-left:17px;
    clip-path:polygon(0 0,100% 0,90% 100%,0 100%)}
  .benefits__list{position:absolute;left:15px;top:485px;list-style:none;width:205px}
  .benefits__item{position:relative;padding-left:19px;font-size:12px;font-weight:500;line-height:13px;
    color:var(--plum);margin-bottom:13.5px;white-space:nowrap}
  .benefits__item::before{content:"";position:absolute;left:0;top:1px;width:9px;height:9px;border:1px solid var(--plum);border-radius:50%}
  .flyer--fr .benefits__item{letter-spacing:-0.2px}
</style>
</head>
<body>

<section class="flyer flyer--en">
  <svg class="flyer__shapes" viewBox="0 0 542 759" aria-hidden="true">
    <path d="M0 335 Q200 420 542 338" fill="none" stroke="var(--plum)" stroke-width="3"/>
    <path d="M0 655 Q150 745 542 733 L542 759 L0 759 Z" fill="var(--plum)"/>
  </svg>
  <div class="photo" role="img" aria-label="Trainer beside an EMS control unit on a stand, with a woman in an EMS training suit"></div>
  <div class="brand">
    <div class="brand__ring"></div>
    <div class="brand__name">Wenna's Atelier</div>
  </div>
  <p class="kicker">Launching</p>
  <h1 class="headline">EMS(Electric Muscle Stimulation)</h1>
  <p class="tagline">A technique that uses electrical impulses to stimulate muscle contractions.</p>
  <p class="event">Alpen Pedal Gathering</p>
  <h2 class="benefits__tag">Benefits:</h2>
  <ul class="benefits__list">
    <li class="benefits__item">Strength training</li>
    <li class="benefits__item">Rehabilitation</li>
    <li class="benefits__item">Pain management</li>
    <li class="benefits__item">Improved circulation</li>
    <li class="benefits__item">Increased muscular<br>endurance</li>
    <li class="benefits__item">Fat loss</li>
  </ul>
</section>

<section class="flyer flyer--fr" lang="fr">
  <svg class="flyer__shapes" viewBox="0 0 542 759" aria-hidden="true">
    <path d="M0 335 Q200 420 542 338" fill="none" stroke="var(--plum)" stroke-width="3"/>
    <path d="M0 655 Q150 745 542 733 L542 759 L0 759 Z" fill="var(--plum)"/>
  </svg>
  <div class="photo" role="img" aria-label="Entraîneur à côté d'un boîtier EMS sur pied, avec une femme en combinaison EMS"></div>
  <div class="brand">
    <div class="brand__ring"></div>
    <div class="brand__name">Wenna's Atelier</div>
  </div>
  <p class="kicker">Lancement</p>
  <h1 class="headline">EMS(Electric Muscle Stimulation)</h1>
  <p class="tagline">Une technique qui utilise des impulsions électriques pour stimuler les contractions musculaires.</p>
  <p class="event">Alpen Pedal Gathering</p>
  <h2 class="benefits__tag">Avantages:</h2>
  <ul class="benefits__list">
    <li class="benefits__item">L'entraînement en force</li>
    <li class="benefits__item">Réhabilitation</li>
    <li class="benefits__item">Gestion de la douleur</li>
    <li class="benefits__item">Amélioration de la circulation</li>
    <li class="benefits__item">Augmentation musculaire<br>endurance</li>
    <li class="benefits__item">La perte de graisse</li>
  </ul>
</section>

</body>
</html>
```